Book Cover Design - Rooted Together: 7 Paths to Raise a Household that Blooms

International cover needed for the Australian (Fenwick Marlow/QRT Press 2011) non-fiction book Rooted Together: 7 Paths to Raise a Household that Blooms.

Blurb: With the birth of a baby, come other new beginnings, the birth of a mother, of a father, and of a family. With each stage of a child's growth, and with every new baby, there are more new beginnings. In older cultures and in villages around the world, parenthood was considered a rite of passage but traditions that guided parents into becoming a family have largely been lost - until now.

This ground breaking book walks a new generation of mothers and fathers through the eight steps of the modern parenthood rite of passage, from couple-connection to family-foundations, so they can prepare for and continue to grow a family that thrives.

Bio: Nora Pembridge is a relationship counsellor, parent educator and columnist for Homeward Nursery magazine. She lives in Sydney with her husband, their three gorgeous children and an itinerary of pets. This is her first book.
Updates

Thank you for your patience, I haven't ever done anything like this before and the designs submitted have helped me to be more specific in my requests. Please see the updated brief. The most important point is that I am seeking a TEXT based cover, so BOTH the TITLE and SUBTITLE should take up most of the space, the image could either be in the background with the title and subtitle overlayed, or be much smaller to fit around them. I have attached some more images to the brief, hope they help to convey the 'feel' I am after.  Thanks again!

Reason: Thank you so much for taking an interest in this project, the process has been very educational and helpful for me. While some of the stock art in the submitted designs are great, I've decided to commission a custom illustration which completely captures the meaning of Rooted Together. I will upload the illustration once it's complete for designers who are still interested to use. Thank you for your patience! Nora

Thank you all for your patience and for opening up my thinking about what I am really hoping for with this cover. I have uploaded some new tree designs and more specific instructions that I would like to be included in the cover design. I'm looking forward to seeing your creations!

With warm regards,

Nora

Target Market(s)

Couples thinking about having a baby and new parents of one or more young children.

Industry/Entity Type

Baby

Requirements
Must have
• TEXT based cover with BOTH the TITLE and SUBTITLE taking up most of the page.
Colors to match the Australian version (see attached)
Tree design bottom left (as per Trunk Treatment image attached) OR Heart Tree Design
Root design (as per one of the two images attached)
PLEASE ADD: three new shoots coming up from the ground under the tree to symbolize the children.
Nice to have
• Artistic effect to complement Australian cover.
Subtle retro feel to complement Australian cover.
Should not have
• The book is inclusive of all parents (including same-sex parents) so no images of mother/father and baby.

```html
<!DOCTYPE html>
<html lang="en">
<head>
<meta charset="utf-8">
<title>Rooted Together — Nora Pembridge</title>
<link rel="stylesheet" href="https://fonts.googleapis.com/css2?family=Arimo:ital@1&family=Crimson+Pro:ital,wght@0,600;0,700;1,500;1,700&display=swap">
<style>
  :root {
    --paper: #ffffff;
    --frame: #1a1a1a;
    --title-red: #c41e32;
    --earth-brown: #3a2414;
    --vine-green: #5e7c3a;
    --vine-light: #a9bd8c;
  }
  html, body {
    margin: 0;
    padding: 0;
    overflow: hidden;
    background: var(--paper);
  }
  .cover {
    position: relative;
    width: 801px;
    height: 1200px;
    background: var(--paper);
    box-sizing: border-box;
    border: 2px solid var(--frame);
    overflow: hidden;
  }
  .title-lead {
    position: absolute;
    top: 62px;
    right: 22px;
    margin: 0;
    font-family: "Arimo", Arial, sans-serif;
    font-style: italic;
    font-weight: 400;
    font-size: 84px;
    line-height: 1;
    letter-spacing: 1px;
    color: var(--title-red);
  }
  .title-main {
    position: absolute;
    top: 150px;
    left: -14px;
    margin: 0;
    font-family: "Crimson Pro", Georgia, serif;
    font-style: italic;
    font-weight: 500;
    font-size: 232px;
    line-height: 1;
    letter-spacing: -8px;
    color: var(--earth-brown);
    white-space: nowrap;
  }
  .vine-art {
    position: absolute;
    top: 462px;
    left: 236px;
    width: 126px;
    height: 250px;
    border-radius: 50px 50px 20px 20px;
    background: radial-gradient(ellipse at 50% 55%, var(--vine-light) 0%, rgba(169,189,140,0.35) 60%, rgba(255,255,255,0) 100%);
  }
  .subtitle {
    position: absolute;
    top: 700px;
    left: 0;
    width: 780px;
    margin: 0;
    font-family: "Crimson Pro", Georgia, serif;
    font-weight: 700;
    font-size: 40px;
    line-height: 55px;
    color: var(--earth-brown);
    text-align: center;
    text-transform: uppercase;
  }
  .subtitle .numeral {
    display: inline-block;
    font-size: 132px;
    line-height: 80px;
    color: var(--vine-green);
    vertical-align: -4px;
    margin-right: 2px;
  }
  .subtitle span.line { display: block; }
  .author {
    position: absolute;
    top: 1112px;
    left: 0;
    width: 801px;
    margin: 0;
    font-family: "Crimson Pro", Georgia, serif;
    font-style: italic;
    font-weight: 700;
    font-size: 42px;
    line-height: 1;
    text-align: center;
    color: var(--earth-brown);
  }
</style>
</head>
<body>
  <main class="cover">
    <h1>
      <span class="title-lead">ROOTED</span>
      <span class="title-main">together!</span>
    </h1>
    <div class="vine-art" role="img" aria-label="Twining green vine illustration growing upward from the numeral"></div>
    <h2 class="subtitle">
      <span class="line"><span class="numeral">7</span>PATHS</span>
      <span class="line">TO RAISE</span>
      <span class="line">A HOUSEHOLD</span>
      <span class="line">THAT</span>
      <span class="line">BLOOMS</span>
    </h2>
    <p class="author">Nora Pembridge</p>
  </main>
</body>
</html>
```